StageLoop - Music Industry App needs a top quality wordpress homepage

We need a modern responsive wordpress homepage built. Our website will only feature one page with the goal to get people to sign up to our app. A word document has been uploaded outlining the page content/sections.

Once the homepage is finalised, I will also need 2 landing pages built as part of this competition. It will be very similar to the homepage with the same layout etc but just feature different images and content. The homepage is for anyone (artists and venues) to find out about us but the landing pages will be artist or venue specific.

The completed work must be delivered as an exportable file into wordpress and be designed properly so no more work is needed to begin utilising as the actual website. The images used must be setup correctly for speed and quality also.

Target Market(s)

Venues and Artists.

Coding

Coded - Design and coding required

Requirements
Must have
• UPDATE: High Res Logo files attached
• Must be a modern looking website and be responsive. Must look good across all devices from desktop, to mobile and tablet. Needs to be very high quality.
• Please see the attached logo - I am waiting for the final high quality version and will reupload when complete but this will be enough to get you started for now. The website must have a dark base colour and have red/white elements to match the logo. The red colour used MUST match the red colour used in the logo.
• Please have a go at creating it how you think is best and provide feedback from there. I am leaving it very open to the designers so I can get the best website possible and lots of different ideas etc.

```html
<!DOCTYPE html>
<html lang="en">
<head>
<meta charset="utf-8">
<title>StageLoop – Zipcab for Live Music</title>
<link href="https://fonts.googleapis.com/css2?family=Arimo:wght@400;700&family=Lato:wght@400;700&display=swap" rel="stylesheet">
<style>
:root{
  --red:#ee1c24;
  --ink:#111111;
  --body:#555555;
  --white:#ffffff;
  --field:#ebebeb;
  --field-line:#d4d4d4;
  --footer:#000000;
}
*{box-sizing:border-box;margin:0;padding:0}
html,body{width:1200px;height:3690px;overflow:hidden;background:var(--white)}
body{position:relative;font-family:"Lato",sans-serif;color:var(--body)}
.abs{position:absolute}
.head{font-family:"Arimo",sans-serif;font-weight:700}

/* hero */
.hero{left:0;top:0;width:1200px;height:637px;
  background:radial-gradient(ellipse at 50% 15%,#7a2a12 0%,#3d1408 45%,#140604 100%)}
.hero-crowd{left:0;top:380px;width:1200px;height:257px;
  background:linear-gradient(180deg,rgba(0,0,0,0) 0%,rgba(10,3,2,.75) 60%,#0b0302 100%)}
.brand{font-family:"Lato",sans-serif;font-weight:700;font-size:24px;color:var(--white);display:flex;align-items:center;gap:8px;white-space:nowrap}
.brand-dot{width:22px;height:22px;border-radius:50%;background:var(--red)}
.nav{top:53px;left:316px;font-family:"Arimo",sans-serif;font-weight:700;font-size:12.5px;color:var(--white)}
.nav span{position:absolute;top:0;white-space:nowrap}
.nav .active{color:var(--red)}
.nav-mark{left:403px;top:0;width:1px;height:38px;background:var(--red)}
.nav-mark::after{content:"";position:absolute;left:-2px;bottom:-2px;width:5px;height:5px;border-radius:50%;background:var(--red)}
.btn-nav{left:918px;top:43px;width:120px;height:38px;background:var(--white);color:var(--red);
  font-family:"Arimo",sans-serif;font-weight:700;font-size:12.5px;display:flex;align-items:center;justify-content:center}
.hero-title{left:0;top:212px;width:1200px;text-align:center;font-size:52px;color:var(--white);white-space:nowrap}
.hero-sub{left:0;top:291px;width:1200px;text-align:center;font-size:16px;color:var(--white)}
.hero-form{left:338px;top:351px;width:523px;height:47px;display:flex}
.hero-form .field{flex:1;background:var(--white);font-size:11px;color:#777;padding-left:14px;display:flex;align-items:center}
.hero-form .go{width:128px;background:var(--red);color:var(--white);font-family:"Arimo",sans-serif;font-weight:700;font-size:17px;display:flex;align-items:center;justify-content:center}
.pager{left:178px;top:557px;font-family:"Arimo",sans-serif;font-weight:700;font-size:15px;color:var(--white);display:flex;align-items:center}
.pager .line{width:62px;height:1px;background:var(--red);margin:0 14px}
.pager .on{color:var(--red)}

/* feature sections */
.photo{display:block}
.title{font-size:40px;color:var(--ink);white-space:nowrap}
.title em{font-style:normal;color:var(--red)}
.points{list-style:none;font-size:11.5px;color:var(--body);white-space:nowrap}
.points li{height:30.2px}

/* pre register */
.card{background:var(--white);box-shadow:0 0 6px rgba(0,0,0,.18)}
.pre-title{left:182px;top:2258px;font-size:34px}
.pre-text{left:182px;top:2302px;font-size:11.5px}
.pre-form{left:180px;top:2338px;width:522px;height:48px;display:flex}
.pre-form .field{flex:1;background:var(--field);border:1px solid var(--field-line);font-size:11.5px;color:#777;padding-left:10px;display:flex;align-items:center}
.pre-form .go{width:126px;background:var(--red);color:var(--white);font-family:"Arimo",sans-serif;font-weight:700;font-size:13px;display:flex;align-items:center;justify-content:center}
.about-title{left:646px;top:2570px;font-size:40px}
.about-text{left:645px;top:2628px;width:378px;font-size:11.5px;line-height:21px}

/* contact */
.contact-title{left:0;top:2868px;width:1200px;text-align:center;font-size:42px}
.input{background:var(--field);border:1px solid var(--field-line);font-size:11.5px;color:#666;padding:12px 13px}
.send{left:536px;top:3185px;width:127px;height:43px;background:var(--red);color:var(--white);font-family:"Arimo",sans-serif;font-weight:700;font-size:13.5px;display:flex;align-items:center;justify-content:center}

/* footer */
.footer{left:0;top:3302px;width:1200px;height:343px;background:var(--footer)}
.map{left:0;top:3302px;width:458px;height:343px;background:linear-gradient(160deg,#a8c9ee 0%,#8fb8e6 45%,#c9dcb8 80%,#d8e3c4 100%)}
.f-head{font-family:"Arimo",sans-serif;font-weight:700;font-size:14px;color:var(--red)}
.f-links{list-style:none;font-family:"Arimo",sans-serif;font-size:12px;color:var(--white)}
.f-links li{height:21px}
.f-text{font-family:"Arimo",sans-serif;font-size:12.5px;color:var(--white);line-height:19px}
.social{display:flex;align-items:center;gap:12px;font-family:"Arimo",sans-serif;font-size:12.5px;color:var(--white)}
.social .ring{width:36px;height:36px;border:1.5px solid var(--white);border-radius:50%}
.legal{left:0;top:3645px;width:1200px;height:45px;background:var(--red);color:var(--white);font-size:11.5px;display:flex;align-items:center;justify-content:center}
.legal b{font-weight:700;margin:0 3px}
</style>
</head>
<body>

<!-- hero -->
<header>
  <div class="abs hero" role="img" aria-label="Concert crowd with hands raised under red stage lights"></div>
  <div class="abs hero-crowd"></div>
  <div class="abs brand" style="left:160px;top:46px"><span class="brand-dot"></span>StageLoop</div>
  <div class="abs nav-mark"></div>
  <nav class="abs nav">
    <span style="left:0">Home</span>
    <span class="active" style="left:68px">About</span>
    <span style="left:139px">Artist</span>
    <span style="left:204px">How its work?</span>
    <span style="left:318px">Why StageLoop?</span>
    <span style="left:431px">Venues</span>
    <span style="left:506px">Contact Us</span>
  </nav>
  <div class="abs btn-nav">Sign Up For Free</div>
  <h1 class="abs head hero-title">‘ZIPCAB FOR LIVE MUSIC’</h1>
  <p class="abs hero-sub">‘StageLoop connects venues with artists to make booking gigs simple’</p>
  <div class="abs hero-form"><div class="field">Enter Email:</div><div class="go">Free Sign Up</div></div>
  <div class="abs pager"><span>01</span>&nbsp;&nbsp;<span>02</span><span class="line"></span><span class="on">03</span>&nbsp;&nbsp;<span>04</span></div>
</header>

<!-- how it works -->
<section>
  <div class="abs photo" style="left:0;top:735px;width:262px;height:336px;background:linear-gradient(180deg,#7fb2d6,#8a8f86 60%,#4e4a44)" role="img" aria-label="Guitarist performing outdoors by the sea"></div>
  <div class="abs photo" style="left:176px;top:758px;width:413px;height:285px;background:radial-gradient(ellipse at 70% 30%,#6ff0c0,#1f9a78 50%,#0b3a30)" role="img" aria-label="Singer at a microphone under green stage light"></div>
  <h2 class="abs head title" style="left:613px;top:786px"><em>How</em> StageLoop works?</h2>
  <ul class="abs points" style="left:613px;top:872px">
    <li>- Artists and venues sign up for free and create a profile.</li>
    <li>- Venues search for an artist for their upcoming gigs.</li>
    <li>- Venues request a quote and communicate with the artist direct.</li>
    <li>- The gig is booked in once payment is provided by the venue.</li>
    <li>- Upon completion the money is paid to the artist within 48 hours or less.</li>
  </ul>
</section>

<!-- why -->
<section>
  <h2 class="abs head title" style="left:162px;top:1180px"><em>Why</em> StageLoop?</h2>
  <ul class="abs points" style="left:162px;top:1259px">
    <li>- StageLoop makes gig booking easy for both the venue and artist.</li>
    <li>- Join the StageLoop community which is full of amazing artists and venues.</li>
    <li>-&nbsp; Everyone is protected with our complimentary dispute resolutions.</li>
    <li>-Get the best rate possible with StageLoop only receiving 5% of the artists fee.</li>
  </ul>
  <div class="abs photo" style="left:941px;top:1110px;width:259px;height:336px;background:linear-gradient(180deg,#c9b497,#9c8466 55%,#6b5a45)" role="img" aria-label="Street guitarist playing in an old town square"></div>
  <div class="abs photo" style="left:611px;top:1133px;width:413px;height:285px;background:radial-gradient(ellipse at 50% 45%,#3b4652,#1b242c 70%)" role="img" aria-label="Person in headphones with tattooed crossed arms"></div>
</section>

<!-- venue -->
<section>
  <div class="abs photo" style="left:0;top:1494px;width:262px;height:336px;background:linear-gradient(135deg,#3a3a3a,#8c8c8c 50%,#2a2a2a)" role="img" aria-label="Black and white photo of a rock singer shouting"></div>
  <div class="abs photo" style="left:176px;top:1516px;width:413px;height:285px;background:linear-gradient(180deg,#f7a21a,#e8561a 55%,#3a1208)" role="img" aria-label="Festival crowd under orange stage lights"></div>
  <h2 class="abs head title" style="left:613px;top:1545px"><em>StageLoop</em> Venue</h2>
  <ul class="abs points" style="left:613px;top:1631px">
    <li>- StageLoop is a 100% FREE service for all venues - you pay us nothing!</li>
    <li>- Get instant access to hundreds of artists around your local community.</li>
    <li>- All genres to suit any venue from a pub to a wedding or even a nightclub.</li>
    <li>- Simple booking process with a money back guarantee.</li>
    <li>- Communicate directly with the artist and negotiate the price.</li>
  </ul>
</section>

<!-- artists -->
<section>
  <h2 class="abs head title" style="left:162px;top:1926px"><em>Our</em> Artists</h2>
  <ul class="abs points" style="left:162px;top:1998px">
    <li>- StageLoop is a 100% FREE service for all venues - you pay us nothing!</li>
    <li>- Negotiate your price and don’t pay huge agent fees to ensure you earn top dollar</li>
    <li>- Sign up to StageLoop for FREE and get yourself in front of venues</li>
    <li>- All genres and artists welcome - as long as you’re experienced</li>
    <li>- Upon completion the money is paid to the artist within 48 hours or less.</li>
  </ul>
  <div class="abs photo" style="left:941px;top:1867px;width:259px;height:337px;background:linear-gradient(135deg,#d9b48f,#9a7a5e 50%,#2b2f36)" role="img" aria-label="Woman wearing over-ear headphones"></div>
  <div class="abs photo" style="left:611px;top:1890px;width:413px;height:285px;background:radial-gradient(ellipse at 55% 50%,#f5c63a,#dba80f 70%)" role="img" aria-label="Woman with headphones dancing against a yellow wall"></div>
</section>

<!-- pre register and about -->
<section>
  <div class="abs photo" style="left:225px;top:2357px;width:975px;height:264px;background:linear-gradient(100deg,#c9a58a 0%,#e6cdb8 35%,#cfd8e2 65%,#8fa6c0 100%)" role="img" aria-label="Close-up of a guitarist playing against a cloudy sky"></div>
  <div class="abs card" style="left:160px;top:2240px;width:565px;height:189px"></div>
  <h2 class="abs head title pre-title"><em>Pre</em> Register</h2>
  <p class="abs pre-text">Pre-register now to keep informed and be one of the first people to use our platform.</p>
  <div class="abs pre-form"><div class="field">Enter Email:</div><div class="go">Pre Register Now</div></div>

  <div class="abs card" style="left:626px;top:2553px;width:414px;height:248px"></div>
  <h2 class="abs head title about-title"><em>About</em> Us</h2>
  <div class="abs about-text">
    <p>Lorem Ipsum is simply dummy text of the printing and typesetting industry. Lorem Ipsum has been the industry’s standard dummy text ever since the 1500s, when an unknown printer took a galley of type and scrambled it to make a type specimen book.</p>
    <p style="margin-top:21px">It has survived not only five centuries, but also the leap into electronic typesetting, remaining essentially unchanged.</p>
  </div>
</section>

<!-- contact -->
<section>
  <h2 class="abs head title contact-title"><em>Contact</em> Us</h2>
  <div class="abs input" style="left:289px;top:2960px;width:300px;height:40px">Name:</div>
  <div class="abs input" style="left:611px;top:2960px;width:300px;height:40px">Email:</div>
  <div class="abs input" style="left:289px;top:3013px;width:300px;height:40px">Phone:</div>
  <div class="abs input" style="left:611px;top:3013px;width:300px;height:40px">Subject:</div>
  <div class="abs input" style="left:289px;top:3065px;width:622px;height:74px">Message:</div>
  <div class="abs send">Send Message</div>
</section>

<!-- footer -->
<footer>
  <div class="abs footer"></div>
  <div class="abs map" role="img" aria-label="Map of the North Atlantic Ocean"></div>
  <div class="abs brand" style="left:484px;top:3333px;font-size:21px"><span class="brand-dot" style="width:18px;height:18px"></span>StageLoop</div>
  <div class="abs f-head" style="left:484px;top:3419px">Quick Link</div>
  <ul class="abs f-links" style="left:484px;top:3456px">
    <li>Home</li><li>About</li><li>Artist</li><li>How its work?</li><li>Why stageloop?</li><li>Vanues</li><li>Contact us</li>
  </ul>
  <div class="abs f-head" style="left:709px;top:3418px;font-size:12.5px">Address:</div>
  <div class="abs f-text" style="left:709px;top:3437px;width:170px">100 - Lorem Ipsum is simply dummy text.</div>
  <div class="abs f-head" style="left:709px;top:3493px;font-size:12.5px">Contact:</div>
  <div class="abs f-text" style="left:709px;top:3513px">+91-000-000-0000</div>
  <div class="abs f-head" style="left:709px;top:3553px;font-size:12.5px">Email:</div>
  <div class="abs f-text" style="left:709px;top:3574px">support@stageloop.com</div>
  <div class="abs social" style="left:896px;top:3419px"><span class="ring"></span>Friendwall</div>
  <div class="abs social" style="left:896px;top:3464px"><span class="ring"></span>WorkLink</div>
  <div class="abs social" style="left:896px;top:3509px"><span class="ring"></span>Clipstream</div>
  <div class="abs social" style="left:896px;top:3555px"><span class="ring"></span>Snapframe</div>
  <div class="abs legal">©2019 <b>StageLoop</b>. All rights reserved. Terms &amp; Conditions | Privacy Policy</div>
</footer>

</body>
</html>
```